I'm looking for an app for customers to order through

I'm looking for an app for my customers to order products through
Ideally each customer would have a customer number with password
Their profile would come up with a preloaded products they currently order
From there they can select the product they require and volume needed for delivery
I would also like an option for them to go to a full product range if they are looking for Ideas or a product they don't currently use
Once the order is completed a copy of the order is them e-mailed to my distribution facilities and a confirmation sent to the customer by e-mail and/or SMS
Current product list is approx 1000 items
Current customers is 80 with expectations to expand to 200
On average current products ordered by each customer is is between 4-8 items
Ordering units are done by both weight and pieces/units

Target Market(s)

Food service outlets,
Restaurant , Hotels, catering companies, clubs, take away shops, cafes
Retail outlets

Number of Pages Required

1 page

Font styles to use
Sans Serif

Colors
abd037

Requirements
Must have
• Customer log in with Password 4 - 6 digit
• Customer order history
Nice to have
• Area for promotions / specials on a weekly / monthly basis

```html
<!DOCTYPE html>
<html lang="en">
<head>
<meta charset="UTF-8">
<title>Re Order – Filters</title>
<link rel="stylesheet" href="https://fonts.googleapis.com/css2?family=Roboto:wght@300;400&display=swap">
<style>
  :root {
    --brand: #abd037;
    --brand-dark: #5a7f1c;
    --fav-tint: #d9ee9b;
    --dairy: #fde68a;
    --meat: #f7958c;
    --fish: #7a9ec9;
    --supplier: #a0a0a0;
    --ink: #1e1e1e;
    --rule: #c8c8c8;
    --paper: #ffffff;
  }
  * { box-sizing: border-box; margin: 0; padding: 0; }
  html, body { width: 675px; height: 1200px; overflow: hidden; background: var(--paper); }
  body { font-family: "Roboto", "Helvetica Neue", Arial, sans-serif; font-weight: 300; color: var(--ink); position: relative; }

  .app-bar { position: absolute; left: 0; top: 0; width: 675px; height: 116px; background: var(--brand); color: #fff; }
  .status { position: absolute; top: 10px; left: 0; width: 100%; height: 24px; font-size: 19px; font-weight: 400; }
  .status .signal { position: absolute; left: 15px; top: 2px; display: flex; align-items: center; gap: 6px; }
  .status .dots { display: flex; gap: 2px; }
  .status .dots span { width: 10px; height: 10px; border-radius: 50%; background: #fff; display: block; }
  .status .time { position: absolute; left: 0; width: 100%; text-align: center; top: 0; }
  .status .battery { position: absolute; right: 14px; top: 2px; }
  .app-title { position: absolute; top: 58px; width: 100%; text-align: center; font-size: 30px; font-weight: 400; }

  .row { position: absolute; left: 0; width: 675px; height: 60px; }
  .badge { position: absolute; left: 53px; top: 4px; width: 52px; height: 52px; border-radius: 50%;
           display: flex; align-items: center; justify-content: center; font-size: 27px; }
  .label { position: absolute; left: 128px; top: 0; line-height: 60px; font-size: 25px; }
  .check { position: absolute; left: 589px; top: 15px; width: 30px; height: 30px; border: 2px solid #333; background: #fff; }

  .badge--fav { background: var(--fav-tint); }
  .badge--dairy { background: var(--dairy); }
  .badge--meat { background: var(--meat); }
  .badge--fish { background: var(--fish); }
  .badge--supplier { background: var(--supplier); }

  .section-title { position: absolute; left: 52px; width: 567px; text-align: center; font-size: 25px; }
  .section-rule { position: absolute; left: 52px; width: 567px; height: 2px; background: var(--rule); }

  .btn { position: absolute; top: 1096px; height: 61px; border: 2px solid #333; background: #fff;
         font-family: inherit; font-size: 22px; font-weight: 400; display: flex; align-items: center; justify-content: center; }
  .btn--cancel { left: 56px; width: 185px; color: var(--ink); }
  .btn--done { left: 414px; width: 200px; border-color: var(--brand-dark); color: var(--brand-dark); }
</style>
</head>
<body>
  <header class="app-bar">
    <div class="status">
      <div class="signal">
        <div class="dots"><span></span><span></span><span></span><span></span><span></span></div>
        <span>Netly</span>
        <svg width="18" height="14" viewBox="0 0 18 14"><path d="M1 5a12 12 0 0 1 16 0M4 8a8 8 0 0 1 10 0M7 11a3.5 3.5 0 0 1 4 0" fill="none" stroke="#fff" stroke-width="2"/></svg>
      </div>
      <div class="time">07:29</div>
      <svg class="battery" width="62" height="20" viewBox="0 0 62 20">
        <rect x="1" y="2" width="40" height="16" rx="3" fill="none" stroke="#fff" stroke-width="2"/>
        <rect x="4" y="5" width="34" height="10" fill="#fff" opacity="0.7"/>
        <rect x="42" y="7" width="3" height="6" fill="#fff"/>
        <path d="M55 1l-6 10h4l-2 8 7-11h-4z" fill="#fff"/>
      </svg>
    </div>
    <h1 class="app-title">Re Order</h1>
  </header>

  <div class="row" style="top:149px">
    <div class="badge badge--fav">
      <svg width="30" height="30" viewBox="0 0 24 24"><path d="M12 1.5l3.1 7.1 7.6.6-5.8 5 1.8 7.5L12 17.7l-6.7 4 1.8-7.5-5.8-5 7.6-.6z" fill="#000"/></svg>
    </div>
    <span class="label" style="left:131px">Only Show Favourites</span>
    <span class="check"></span>
  </div>

  <h2 class="section-title" style="top:245px; font-weight:300">Food Type</h2>
  <div class="section-rule" style="top:287px"></div>

  <div class="row" style="top:317px"><div class="badge badge--dairy">D</div><span class="label">Dairy</span><span class="check" style="left:590px"></span></div>
  <div class="row" style="top:400px"><div class="badge badge--meat">M</div><span class="label">Meat</span><span class="check" style="left:590px"></span></div>
  <div class="row" style="top:484px"><div class="badge badge--fish">F</div><span class="label">Fish</span><span class="check" style="left:590px"></span></div>

  <h2 class="section-title" style="top:578px; font-weight:300">Supplier</h2>
  <div class="section-rule" style="top:622px"></div>

  <div class="row" style="top:650px"><div class="badge badge--supplier"></div><span class="label" style="left:130px">Supplier One</span><span class="check"></span></div>
  <div class="row" style="top:728px"><div class="badge badge--supplier"></div><span class="label" style="left:130px">Supplier Two</span><span class="check"></span></div>
  <div class="row" style="top:803px"><div class="badge badge--supplier"></div><span class="label" style="left:127px">Supplier Three</span><span class="check" style="top:26px"></span></div>

  <button class="btn btn--cancel" type="button">Cancel</button>
  <button class="btn btn--done" type="button">Done</button>
</body>
</html>
```